VELTRIX Web Page

We need a corporate web site for a new company VELTRIX Corporation. VELTRIX is a technology company that has developed a new virtualization solution for corporate applications. Our target customers are IT professionals. We have a logo, which we will provide.

Final design should communicate: innovation, stability, professionalism

Industry/Entity Type

It Company

```html
<!DOCTYPE html>
<html lang="en">
<head>
<meta charset="utf-8">
<title>VELTRIX Corporation</title>
<link rel="stylesheet" href="https://fonts.googleapis.com/css2?family=Open+Sans:wght@400;600;700&display=swap">
<style>
  :root {
    --brand-blue: #2b7fd2;
    --nav-navy: #1c3766;
    --accent-orange: #f7941d;
    --text-dark: #1a1a1a;
    --white: #ffffff;
    --footer-bg: #2d2d2d;
    --footer-link: #3b93e0;
    --slide-panel: rgba(12, 28, 82, 0.72);
    --caption-band: rgba(30, 40, 48, 0.78);
  }
  * { margin: 0; padding: 0; box-sizing: border-box; }
  html, body { width: 1200px; height: 838px; overflow: hidden; background: var(--white); }
  body { font-family: "Open Sans", Arial, sans-serif; color: var(--text-dark); position: relative; }
  a { text-decoration: none; color: inherit; }

  .site-header { position: absolute; top: 0; left: 0; width: 1200px; height: 55px; background: var(--white); }
  .brand-name { position: absolute; left: 103px; top: 10px; font-size: 26px; font-weight: 700; color: var(--brand-blue); letter-spacing: 0.2px; }
  .main-nav { position: absolute; left: 648px; top: 17px; font-size: 16px; color: var(--nav-navy); }
  .main-nav a.is-active { color: var(--accent-orange); }
  .main-nav .sep { margin: 0 8px; }

  .hero { position: absolute; top: 55px; left: 0; width: 1200px; height: 376px; overflow: hidden; }
  .hero-visual { position: absolute; inset: 0;
    background:
      radial-gradient(circle at 235px 180px, #eaf6ff 0, #8fd0ff 60px, #2f8df0 140px, rgba(20,90,230,0) 230px),
      linear-gradient(100deg, #5ab6f5 0%, #1c6fe6 35%, #0c4fd8 65%, #0a2fb0 100%);
  }
  .slider-arrow { position: absolute; top: 142px; width: 50px; height: 50px; }
  .slider-arrow.prev { left: 83px; }
  .slider-arrow.next { left: 1053px; }
  .slide-panel { position: absolute; left: 554px; top: 172px; width: 476px; height: 181px; background: var(--slide-panel); }
  .slide-title { position: absolute; left: 13px; top: 28px; font-size: 24px; font-weight: 700; color: var(--white); }
  .slide-text { position: absolute; left: 12px; top: 73px; width: 415px; font-size: 11.3px; line-height: 13.6px; font-weight: 700; color: var(--white); }
  .read-more { font-weight: 700; color: var(--accent-orange); font-size: 14px; }
  .slide-panel .read-more { position: absolute; left: 339px; top: 149px; }

  .info-block { position: absolute; }
  .info-title { font-size: 18px; font-weight: 600; line-height: 20px; }
  .info-subtitle { font-size: 12px; line-height: 14px; }
  .info-text { font-size: 11.5px; line-height: 14.2px; }
  .block-left { left: 50px; top: 454px; width: 545px; }
  .block-left .info-title, .block-left .info-subtitle { padding-left: 5px; }
  .block-left .info-text { margin-top: 17px; }
  .block-left .info-text + .info-text { margin-top: 14px; }
  .block-right { left: 895px; top: 457px; width: 255px; }
  .block-right .info-text { margin-top: 20px; }
  .info-block .read-more { display: block; text-align: right; font-size: 15px; margin-top: 14px; }
  .block-left .read-more { margin-right: 19px; }
  .block-right .read-more { margin-top: 18px; margin-right: 4px; }

  .feature-card { position: absolute; left: 608px; top: 473px; width: 270px; height: 222px; overflow: hidden; }
  .feature-visual { position: absolute; inset: 0; background: radial-gradient(circle at 150px 80px, #bfe6f7 0, #5fa8c8 70px, #1f4f6a 170px, #0e2a3c 260px); }
  .feature-caption { position: absolute; left: 0; top: 150px; width: 270px; height: 72px; background: var(--caption-band); }
  .feature-caption p { position: absolute; left: 6px; top: 5px; font-size: 20px; line-height: 25px; color: var(--white); }
  .feature-caption .read-more { position: absolute; right: 8px; top: 50px; font-size: 15px; }

  .site-footer { position: absolute; left: 0; top: 738px; width: 1200px; height: 100px; background: var(--footer-bg); text-align: center; }
  .social-links { position: absolute; left: 605px; top: 20px; height: 22px; }
  .social-links span { position: absolute; top: 0; width: 22px; height: 22px; border-radius: 3px; }
  .social-a { left: 0; background: #3b5b9a; }
  .social-b { left: 34px; background: #f08a1c; }
  .social-c { left: 69px; background: #3fa8e0; }
  .footer-nav { position: absolute; left: 0; width: 1200px; top: 44px; font-size: 16px; color: var(--footer-link); }
  .footer-nav a.is-active { color: var(--accent-orange); }
  .footer-nav .sep { margin: 0 9px; }
  .copyright { position: absolute; left: 0; width: 1200px; top: 80px; font-size: 9px; color: var(--white); }
</style>
</head>
<body>
  <header class="site-header">
    <div class="brand-name">VELTRIX Corporation</div>
    <nav class="main-nav">
      <a class="is-active" href="#">Home</a><span class="sep">|</span><a href="#">About us</a><span class="sep">|</span><a href="#">Solutions</a><span class="sep">|</span><a href="#">Contact us</a><span class="sep">|</span><a href="#">Help</a>
    </nav>
  </header>

  <section class="hero">
    <div class="hero-visual" role="img" aria-label="Glowing blue globe over a technology backdrop of light waves and stars"></div>
    <svg class="slider-arrow prev" viewBox="0 0 50 50" aria-label="Previous slide">
      <circle cx="25" cy="25" r="24" fill="#3e5f9e" stroke="#2a4580" stroke-width="2"/>
      <path d="M31 14 L17 25 L31 36" fill="none" stroke="#fff" stroke-width="5" stroke-linecap="round" stroke-linejoin="round"/>
    </svg>
    <svg class="slider-arrow next" viewBox="0 0 50 50" aria-label="Next slide">
      <circle cx="25" cy="25" r="24" fill="#13327a" stroke="#0c2360" stroke-width="2"/>
      <path d="M19 14 L33 25 L19 36" fill="none" stroke="#fff" stroke-width="5" stroke-linecap="round" stroke-linejoin="round"/>
    </svg>
    <div class="slide-panel">
      <h2 class="slide-title">SLIDE 1 INFORMATION</h2>
      <p class="slide-text">The human species' use of technology began with the conversion of natural resources&nbsp; into simple tools. The prehistorical discovery of the ability to control fire increased&nbsp; the available sources of food and the invention of the wheel helped humans</p>
      <a class="read-more" href="#">READ MORE....</a>
    </div>
  </section>

  <article class="info-block block-left">
    <h3 class="info-title">Main Information Title</h3>
    <p class="info-subtitle">sub title</p>
    <p class="info-text">The human species' use of technology began with the conversion of natural resources into simple tools. The prehistorical discovery of the ability to control fire increased the available sources of food and the invention of the wheel helped humans in travelling in and controlling their environment. Recent technological developments, including the printing press, the telephone, and the Internet, have lessened physical barriers to communication and allowed humans to interact freely on a global scale. However, not all technology has been used for peaceful purposes; the development of weapons of ever- increasing destructive power has progressed throughout history, from clubs to nuclear weapons.</p>
    <p class="info-text">The human species' use of technology began with the conversion of natural resources into simple tools. The prehistorical discovery of the ability to control fire increased the available sources of food and the invention of the wheel helped humans in travelling in and controlling their environment.</p>
    <a class="read-more" href="#">READ MORE....</a>
  </article>

  <figure class="feature-card">
    <div class="feature-visual" role="img" aria-label="Hand touching glowing translucent interface tiles"></div>
    <figcaption class="feature-caption">
      <p>Recent technological<br>developments</p>
      <a class="read-more" href="#">READ MORE....</a>
    </figcaption>
  </figure>

  <article class="info-block block-right">
    <h3 class="info-title">Main Information Title</h3>
    <p class="info-subtitle">sub title</p>
    <p class="info-text">Recent technological developments, including<br>the printing press, the telephone, and the<br>Internet, have lessened physical barriers<br>to communication and allowed humans<br>to interact freely on a<br>global scale. However, not all technology<br>has been used for peaceful purposes; the<br>development of weapons of ever-<br>increasing destructive power has<br>progressed throughout history,<br>from clubs to nuclear weapons.</p>
    <a class="read-more" href="#">READ MORE....</a>
  </article>

  <footer class="site-footer">
    <div class="social-links">
      <span class="social-a" aria-label="Social link"></span>
      <span class="social-b" aria-label="Feed link"></span>
      <span class="social-c" aria-label="Social link"></span>
    </div>
    <nav class="footer-nav">
      <a class="is-active" href="#">Home</a><span class="sep">|</span><a href="#">About us</a><span class="sep">|</span><a href="#">Solutions</a><span class="sep">|</span><a href="#">Contact us</a><span class="sep">|</span><a href="#">Help</a>
    </nav>
    <p class="copyright">c2013 VELTRIX Corporation</p>
  </footer>
</body>
</html>
```